Camp Willowmere 2018

We need a postcard design to advertise our summer programs. We are a Christian camp with day camp and overnight camps.

Target Market(s)

parents of elementary age kids

Industry/Entity Type

Christian

Colors
ec1f27
f37122
faa54b
fbee3d
f78f20
f04a50
fbed22
fbee3e

Requirements
Must have
• Day Camp 2018 "Shine Bright Together"
• June 25 - August 24
• $135 per week
• Mon-Fri 8 am to 4 pm. Open to all kids entering grades 1 to 8. Day camp is chock full of activities like swimming, rock wall, archery, sports, crafts, air rifles and much more! Daily lunch and snack included. Before and after-care available at an extra rate.
• Register and pay in full by April 1st, save $270!
• Overnight Camp 2018
• July 15 - 21 & July 22 - 28
• $330 per week
• Open to all kids ages 8 to 14. Spend the week making new friends, sleeping in cabins, climbing the rock wall and swimming at the beach! Our guest speakers will lead twice daily chapel sessions that will challenge campers to grow in their faith.
• 41 Cedar Bluff Rd. Barrington, NH 03817
• 603-418-5296
• www.willowmere-example.org
Nice to have
• bright and colorful

```html
<!DOCTYPE html>
<html lang="en">
<head>
<meta charset="utf-8">
<title>Camp Willowmere 2018 Postcard</title>
<link href="https://fonts.googleapis.com/css2?family=Oswald:wght@500;600;700&family=Josefin+Sans:wght@400;600;700&family=Great+Vibes&display=swap" rel="stylesheet">
<style>
  :root {
    --red: #d21f2b;
    --orange-red: #e0401a;
    --brown: #6b4a2b;
    --ink: #1c1c1c;
    --blush: #fbe4e8;
    --paper: #ffffff;
    --stage: #e6e6e6;
  }
  * { box-sizing: border-box; margin: 0; padding: 0; }
  html, body { width: 1200px; height: 675px; overflow: hidden; }
  body { background: var(--stage); font-family: "Josefin Sans", sans-serif; }

  .sheet { position: relative; width: 1200px; height: 675px; }

  .postcard {
    position: absolute; top: 127px; width: 560px; height: 420px;
    background: var(--paper); overflow: hidden;
    box-shadow: 0 2px 6px rgba(0,0,0,.18);
  }
  .postcard--front { left: 25px; }
  .postcard--back { left: 615px; }
  .postcard__art { position: absolute; inset: 0; }

  /* Front */
  .front-copy {
    position: absolute; right: 26px; top: 24px; width: 320px;
    text-align: right;
  }
  .front-copy__title {
    font-family: "Oswald", sans-serif; font-weight: 700; font-size: 27px;
    color: var(--red); line-height: 1; letter-spacing: .2px;
  }
  .front-copy__tagline {
    font-family: "Great Vibes", cursive; font-size: 28px; color: var(--brown);
    line-height: 1.05; margin-top: 1px;
  }
  .date-bar {
    display: inline-block; background: var(--orange-red); color: #fff;
    font-family: "Josefin Sans", sans-serif; font-weight: 600; font-size: 15px;
    letter-spacing: 1.2px; padding: 5px 6px 2px; margin-top: 3px;
  }
  .price {
    font-family: "Josefin Sans", sans-serif; font-weight: 700; font-size: 40px;
    color: var(--red); line-height: 1; margin-top: 8px;
  }
  .price-unit {
    font-family: "Josefin Sans", sans-serif; font-weight: 400; font-size: 19px;
    color: var(--brown); line-height: 1;
  }
  .front-copy__body {
    font-size: 9.6px; line-height: 1.3; color: var(--ink);
    width: 212px; margin: 9px 0 0 auto;
  }
  .promo__line {
    font-family: "Oswald", sans-serif; font-weight: 500; font-size: 14.5px;
    color: var(--ink); margin-top: 12px; line-height: 1; letter-spacing: -.2px;
  }
  .promo__save {
    font-family: "Josefin Sans", sans-serif; font-weight: 700; font-size: 38px;
    color: var(--orange-red); line-height: 1; margin-top: 6px;
  }
  .brand {
    position: absolute; right: 26px; bottom: 22px;
    display: flex; align-items: center; gap: 10px;
  }
  .brand__dot { width: 22px; height: 22px; border-radius: 50%; background: var(--red); }
  .brand__name {
    font-family: "Josefin Sans", sans-serif; font-weight: 700; font-size: 27px;
    color: var(--red); line-height: 1.05; text-align: right;
  }

  /* Back */
  .back-headline {
    position: absolute; left: 24px; top: 96px;
    font-family: "Oswald", sans-serif; font-weight: 700; font-size: 33px;
    line-height: 1.05; color: var(--red);
    text-shadow: -2px -2px 0 #fff, 2px -2px 0 #fff, -2px 2px 0 #fff, 2px 2px 0 #fff, 0 2px 0 #fff, 2px 0 0 #fff, 0 -2px 0 #fff, -2px 0 0 #fff;
  }
  .back-date {
    position: absolute; left: 24px; top: 172px;
    background: var(--orange-red); color: #fff;
    font-family: "Oswald", sans-serif; font-weight: 500; font-size: 14px;
    padding: 2px 7px; letter-spacing: .2px;
  }
  .back-price { position: absolute; left: 22px; top: 200px; text-align: left; }
  .back-price .price { margin-top: 0; }
  .back-body {
    position: absolute; left: 24px; top: 262px; width: 250px;
    font-size: 9.2px; line-height: 1.25; color: var(--ink); text-align: justify;
  }
  .contact {
    position: absolute; left: 22px; top: 320px; display: flex;
  }
  .contact__item { padding-right: 8px; }
  .contact__item + .contact__item { border-left: 1px solid var(--ink); padding-left: 8px; }
  .contact__label {
    font-family: "Oswald", sans-serif; font-weight: 600; font-size: 15px;
    color: var(--ink); line-height: 1.1;
  }
  .contact__value {
    font-family: "Oswald", sans-serif; font-weight: 600; font-size: 15px;
    color: var(--red); line-height: 1.1;
  }
  .address {
    position: absolute; left: 24px; top: 358px;
    font-family: "Josefin Sans", sans-serif; font-weight: 600; font-size: 10.5px;
    color: var(--ink); line-height: 1;
  }
</style>
</head>
<body>
<main class="sheet">

  <!-- Front of postcard -->
  <section class="postcard postcard--front">
    <svg class="postcard__art" viewBox="0 0 560 420">
      <defs>
        <linearGradient id="portraitTones" x1="0" y1="0" x2="1" y2="1">
          <stop offset="0" stop-color="#a89a88"/>
          <stop offset=".45" stop-color="#d9b49a"/>
          <stop offset="1" stop-color="#6f655c"/>
        </linearGradient>
      </defs>
      <path d="M285 0 H335 C300 90 335 170 305 260 C285 330 300 380 335 420 H200 C190 360 195 280 225 200 C248 140 250 60 285 0Z" fill="var(--blush)"/>
      <path role="img" aria-label="Photo of a smiling girl camper in front of a tree" d="M0 0 H285 C250 60 248 140 225 200 C195 280 190 360 200 420 H0Z" fill="url(#portraitTones)"/>
    </svg>

    <div class="front-copy">
      <h1 class="front-copy__title">DAY CAMP 2018</h1>
      <p class="front-copy__tagline">Shine Bright Together</p>
      <p class="date-bar">JUNE 25 – AUGUST 24</p>
      <p class="price">$135</p>
      <p class="price-unit">PER WEEK</p>
      <p class="front-copy__body">Mon-Fri 8 am to 4 pm. Open to kids entering grades 1 to 8. Day camp is chock full of activities like swimming, rock wall, archery, sports, crafts, air rifles and much more! Daily lunch and snack included. Before and after-care available at an extra rate.</p>
      <p class="promo__line">REGISTER &amp; PAY IN FULL BY APRIL 1ST</p>
      <p class="promo__save">SAVE $270</p>
    </div>

    <div class="brand">
      <span class="brand__dot"></span>
      <p class="brand__name">Camp<br>Willowmere</p>
    </div>
  </section>

  <!-- Back of postcard -->
  <section class="postcard postcard--back">
    <svg class="postcard__art" viewBox="0 0 560 420">
      <defs>
        <linearGradient id="beachTones" x1="0" y1="0" x2="1" y2="1">
          <stop offset="0" stop-color="#8f8a72"/>
          <stop offset=".6" stop-color="#b7a58d"/>
          <stop offset="1" stop-color="#6f7a5c"/>
        </linearGradient>
        <linearGradient id="boyTones" x1="0" y1="0" x2="1" y2="1">
          <stop offset="0" stop-color="#5f7a3e"/>
          <stop offset="1" stop-color="#e0b99a"/>
        </linearGradient>
        <linearGradient id="lakeTones" x1="0" y1="0" x2="0" y2="1">
          <stop offset="0" stop-color="#c9a58a"/>
          <stop offset="1" stop-color="#6f7d6a"/>
        </linearGradient>
      </defs>
      <path role="img" aria-label="Photo of campers sitting on a beach by the lake" d="M0 0 H255 C235 60 225 120 195 170 C150 175 80 178 0 172Z" fill="url(#beachTones)"/>
      <circle cx="230" cy="57" r="62" fill="var(--red)"/>
      <circle role="img" aria-label="Photo of a smiling boy camper" cx="232" cy="57" r="57" fill="url(#boyTones)"/>
      <circle cx="230" cy="180" r="67" fill="var(--red)"/>
      <circle role="img" aria-label="Photo of a boy swimming in the lake" cx="234" cy="176" r="62" fill="url(#lakeTones)"/>
      <path d="M0 389 C120 372 280 370 400 382 C480 390 530 392 560 386 V420 H0Z" fill="var(--red)"/>
    </svg>

    <h2 class="back-headline">OVERNIGHT<br>CAMP 2018</h2>
    <p class="back-date">JULY 15 – 21 &amp; JULY 22 – 28</p>
    <div class="back-price">
      <p class="price">$330</p>
      <p class="price-unit">PER WEEK</p>
    </div>
    <p class="back-body">Open to kids ages 8 to 14. Spend the week making new friends, sleeping in cabins, climbing the rock wall and swimming at the beach! Our guest speakers will lead twice daily chapel sessions that will challenge campers to grow in their faith.</p>
    <div class="contact">
      <div class="contact__item">
        <p class="contact__label">CALL US</p>
        <p class="contact__value">603-418-5296</p>
      </div>
      <div class="contact__item">
        <p class="contact__label">VISIT US</p>
        <p class="contact__value">WWW.WILLOWMERE-EXAMPLE.ORG</p>
      </div>
    </div>
    <p class="address">41 Cedar Bluff Rd. Barrington, NH 03817</p>
  </section>

</main>
</body>
</html>
```